Business card design only (Have Logo Online) Shoudl be quick and easy for designer

We would like to have a business card design that is in-line with our company logo. Final deliverables should include two EPS extension file. One for the front card design and the other the back-end design. Please also indicate the font style used.

Advisory Pebble is a social enterprise that focuses on utilizing technology, unique methodologies and international partnerships to provide a one-stop location for economical and dependable IT-related solutions.

Target Market(s)

Micro, small and medium business owners.

Industry/Entity Type

Business

Requirements
Must have
• The business card should incorporate our company logo.
Nice to have
• A little web 2.0 style would be nice but I haven''t decided yet.

```html
<!DOCTYPE html>
<html lang="en">
<head>
<meta charset="utf-8">
<title>Advisory Pebble – Business Card</title>
<link rel="stylesheet" href="https://fonts.googleapis.com/css2?family=Arimo:wght@400;700&display=swap">
<style>
  :root {
    --sheet: #e0e0e0;
    --card: #ffffff;
    --green-dark: #3f8a55;
    --green-light: #9fd18f;
    --green-soft: #8fcf86;
    --white: #ffffff;
  }
  * { margin: 0; padding: 0; box-sizing: border-box; }
  html, body {
    width: 1060px;
    height: 1200px;
    overflow: hidden;
  }
  body {
    position: relative;
    background: var(--sheet);
    font-family: "Arimo", Arial, sans-serif;
  }
  .card {
    position: absolute;
    left: 29px;
    width: 1002px;
    background: var(--card);
    overflow: hidden;
  }
  .card--front { top: 29px; height: 555px; }
  .card--back  { top: 614px; height: 556px; }

  /* Front */
  .brand {
    position: absolute;
    top: 182px;
    left: 0;
    width: 100%;
    display: flex;
    justify-content: center;
    align-items: center;
    gap: 18px;
  }
  .brand__dot {
    width: 56px;
    height: 56px;
    border-radius: 50%;
    background: var(--green-light);
  }
  .brand__name {
    font-size: 52px;
    font-weight: 700;
    color: var(--green-dark);
    letter-spacing: 1px;
  }
  .tagline {
    position: absolute;
    top: 378px;
    width: 100%;
    text-align: center;
    font-size: 53px;
    color: var(--green-dark);
  }
  .subline {
    position: absolute;
    top: 452px;
    width: 100%;
    text-align: center;
    font-size: 23px;
    color: var(--green-soft);
  }

  /* Back */
  .person {
    position: absolute;
    top: 116px;
    width: 100%;
    text-align: center;
  }
  .person__name {
    font-size: 60px;
    font-weight: 700;
    color: var(--green-dark);
    line-height: 1.1;
  }
  .person__role {
    font-size: 36px;
    color: var(--green-soft);
    line-height: 1.1;
    margin-top: 4px;
  }
  .contact-band {
    position: absolute;
    left: 0;
    bottom: 0;
    width: 100%;
    height: 237px;
    background: var(--green-light);
  }
  .contact-list {
    position: absolute;
    top: 44px;
    left: 0;
    display: grid;
    grid-template-columns: 277px auto;
    column-gap: 20px;
    row-gap: 0;
    font-size: 27px;
    line-height: 35px;
  }
  .contact-list dt {
    text-align: right;
    color: var(--green-dark);
  }
  .contact-list dd {
    color: var(--white);
  }
</style>
</head>
<body>
  <section class="card card--front">
    <div class="brand">
      <span class="brand__dot" aria-hidden="true"></span>
      <span class="brand__name">Advisory Pebble</span>
    </div>
    <p class="tagline">Building with you!</p>
    <p class="subline">Offering practical, honest and dependable solutions for every budget</p>
  </section>

  <section class="card card--back">
    <div class="person">
      <h1 class="person__name">Marlon Teague</h1>
      <p class="person__role">founder</p>
    </div>
    <div class="contact-band">
      <dl class="contact-list">
        <dt>address:</dt><dd>2184 Alder Lane, BC Canada, V3K 2P9</dd>
        <dt>web:</dt><dd>www.advisorypebble.com</dd>
        <dt>cell:</dt><dd>1 604 555 0148</dd>
        <dt>e-mail:</dt><dd>marlon.teague@advisorypebble.com</dd>
      </dl>
    </div>
  </section>
</body>
</html>
```